Short-Term Rental Website - Management Services for Property Owner

We are looking for a website to advertise our short-term rental business, Bright Harbor Rental Management, currently www.brightharbor.ca. Hosted on WordPress.

We have the website main page language but we are looking for someone who is creative and can present the information in a trendy, cool and professional way. I like the closed design crowd job "Tallowfern Marketing - SEM, Influencer website. BOLD GROOVY TONES" (see attached pictures) in terms of how the page flows, icons and stock images, other connective imagery and design features

Our main competitor website is www.stayplume.com and we like how that website feels but we like the elegance of www.Dravona-Kessler.com (desktop) and main page of www.morlane.ca (desktop version). We like the slow type video on morlane.com.

MUST LOOK GOOD ON MOBILE. The mobile experience has to be good.

The content in terms of the language is in one of the attached files.

Our landing page requires the following sections;
- Revenue Maximization
- Services (I have included the content that we want highlighted but we are looking for someone to be creative with how these are displayed
- Pricing
- Featured Properties (display on a carousel) *must design a carousel that can be easily populated.
- Reviews (display on a carousel) *must design a carousel that can be easily populated.
- Contact Us (first name, last name, email, phone (required), description of property)

The header will have;
- Logo (link to main page)
- Pricing (link to pricing section found on the main page)
- Services (link to services section found on the main page)
- Properties (separate page)
- Contact (link to contact area on main page)

We would also need a coded template page that we could use to add additional pages as needed.

For the properties page, we need a landing page that would allow our guests to see all of our properties and a map view with the properties plotted on the map.

As we would collect personal information we would need a cookies/ privacy policy.

The colour palette should be on the light side. We do not want the website to have a dark feel. Colours should be consistent with that of our logo but we are open to creativity.

Target Market(s)

Investment property owners

Industry/Entity Type

Real Estate

Coding

Coded - Design and coding required

Number of Pages Required

2 page

Font styles to use
Sans Serif

Requirements
Must have
• Very strong and well designed landing page

Second page which showcases properttes

Template property page that can be easily reproduced

```html
<!DOCTYPE html>
<html lang="en">
<head>
<meta charset="utf-8">
<title>Bright Harbor Rental Management</title>
<link rel="stylesheet" href="https://fonts.googleapis.com/css2?family=Poppins:wght@400;500;600;700&display=swap">
<style>
:root{
  --blue:#3c5fb1;
  --blue-deep:#2f4f9f;
  --navy:#262b3b;
  --ink:#1f2230;
  --text:#555a66;
  --muted:#8a8f99;
  --light:#eef0f5;
  --white:#ffffff;
  --orange:#f5a623;
  --star:#f39c12;
}
*{box-sizing:border-box;margin:0;padding:0}
html,body{width:1200px;height:4658px;overflow:hidden}
body{position:relative;font-family:"Poppins",sans-serif;color:var(--ink);background:var(--white)}
.abs{position:absolute}
.center{left:0;width:1200px;text-align:center}
.btn{position:absolute;display:flex;align-items:center;justify-content:center;gap:8px;font-size:15px;border-radius:3px}
.btn-solid{background:var(--blue);color:var(--white)}
.btn-ghost{border:1.5px solid #9aa0ab;color:var(--ink);background:var(--white)}
.btn-grey{background:#9aa3b3;color:var(--white)}

/* hero */
.hero{left:0;top:0;width:1200px;height:678px;background:linear-gradient(180deg,#7aa0c7 0%,#b6cde0 40%,#c9cfd3 70%,#8f979c 100%)}
.logo{display:flex;align-items:center;gap:10px;color:var(--white);font-weight:700;font-size:36px;letter-spacing:-.5px;white-space:nowrap}
.logo-mark{width:36px;height:36px;border:4px solid currentColor;border-radius:4px}
.nav{top:78px;font-size:14px;font-weight:600;color:var(--white)}
.nav span{position:absolute;white-space:nowrap}
.nav .sep{width:1px;height:18px;background:rgba(255,255,255,.5);top:0}
.social{width:24px;height:24px;border-radius:50%}
.hero-arrow{width:40px;height:40px;border-radius:50%;border:2px solid var(--white);background:rgba(60,95,177,.6);display:flex;align-items:center;justify-content:center}
.hero h1{top:465px;font-size:50px;font-weight:700;color:var(--white)}
.hero .sub{top:532px;font-size:27px;color:var(--white)}

/* intro */
.intro-photo{left:190px;top:728px;width:310px;height:315px;border-radius:34px;background:linear-gradient(135deg,#9fb0c8,#d9dde2 55%,#b9a594)}
.intro-shadow{left:240px;top:1070px;width:230px;height:18px;border-radius:50%;background:radial-gradient(closest-side,rgba(0,0,0,.25),transparent)}
.intro-text{left:640px;width:430px}
.intro h2{top:752px;font-size:35px;font-weight:500;line-height:1.25}
.intro .lead{top:855px;font-size:16px;font-weight:600;line-height:1.7}
.intro .body{top:918px;font-size:13px;line-height:2.1;color:var(--text)}

/* services */
.services{left:0;top:1229px;width:1200px;height:976px;background:linear-gradient(180deg,#5673b3,#4a67ab 60%,#5874b2)}
.svc{position:absolute;width:294px;height:290px;clip-path:polygon(0 26px,50% 0,100% 26px,100% 100%,0 100%);background:rgba(255,255,255,.18);color:var(--white);text-align:center;padding:36px 24px 0}
.svc.active{background:var(--blue)}
.svc-icon{width:82px;height:82px;border-radius:50%;margin:0 auto 12px;background:#3e4452;border:3px solid rgba(255,255,255,.6);display:flex;align-items:center;justify-content:center}
.svc.active .svc-icon{background:var(--white)}
.svc h3{font-size:18px;font-weight:600;line-height:1.25;margin-bottom:12px}
.svc p{font-size:13px;line-height:1.75}

/* pricing */
.pricing{left:0;top:2205px;width:1200px;height:804px;background:var(--blue)}
.plan{position:absolute;background:var(--white);text-align:center;padding-top:54px}
.plan .tag{display:inline-block;background:var(--orange);color:var(--white);font-size:11px;padding:5px 14px;border-radius:2px;margin-bottom:14px}
.plan h4{font-size:15px;font-weight:500}
.plan .price{font-size:46px;font-weight:700;margin:10px 0 16px}
.plan .price small{font-size:16px;font-weight:500}
.plan .price sup{font-size:18px;vertical-align:-6px}
.plan ul{list-style:none;text-align:left;padding-left:30px;font-size:12px;color:var(--text)}
.plan li{display:flex;gap:10px;align-items:center;margin-bottom:12px}

/* featured */
.featured h2{top:3050px;font-size:34px;font-weight:600}
.prop{position:absolute;width:305px;height:355px;background:var(--white);box-shadow:0 4px 22px rgba(0,0,0,.1)}
.prop-img{position:absolute;left:8px;top:8px;width:289px;height:194px}
.prop h5{position:absolute;left:0;top:222px;width:305px;text-align:center;font-size:16px;font-weight:500;line-height:1.5}
.prop .meta{position:absolute;left:16px;right:16px;top:293px;display:flex;align-items:center;font-size:12px;color:var(--muted)}
.prop .meta b{font-size:17px;color:var(--ink);font-weight:600;flex:1}
.prop .btn{left:90px;top:335px;width:125px;height:38px;font-size:13px}
.side-arrow{width:34px;height:34px;border-radius:50%;border:1.5px solid #9aa0ab;display:flex;align-items:center;justify-content:center}
.dots{display:flex;gap:7px;justify-content:center}
.dots i{width:10px;height:10px;border-radius:50%;border:1px solid #9aa0ab}
.dots i.on{background:var(--blue);border-color:var(--blue)}

/* reviews */
.reviews-bg{left:0;top:3668px;width:1200px;height:669px;background:linear-gradient(180deg,#f3f4f6,#e4d9cf 55%,#d8c8b8)}
.reviews h2{top:3782px;font-size:34px;font-weight:600}
.review{position:absolute;width:276px;height:190px;background:var(--white);text-align:center;padding:22px 30px 0}
.review .stars{color:var(--star);font-size:18px;letter-spacing:2px}
.review h6{font-size:12px;font-weight:600;margin:8px 0 12px}
.review p{font-size:11px;line-height:1.8;color:var(--text)}
.person{position:absolute;width:200px;text-align:center;font-size:12px}
.avatar{width:58px;height:58px;border-radius:50%;margin:0 auto 6px;background:linear-gradient(135deg,#bcc4cf,#7d8796);border:3px solid var(--white)}
.person b{font-weight:600;display:block}

/* footer */
.footer{left:0;top:4337px;width:1200px;height:321px;background:var(--navy);color:var(--white)}
.footer-phone{left:840px;top:4500px;width:178px;height:44px;border-radius:3px;background:var(--blue);display:flex;align-items:center;font-size:15px}
.footer-phone i{width:44px;height:44px;border-radius:50%;background:var(--navy);border:2px solid var(--white);display:flex;align-items:center;justify-content:center;margin-left:-1px;margin-right:14px}
</style>
</head>
<body>

<!-- HERO -->
<section class="abs hero">
  <div class="abs" role="img" aria-label="Hero photo: couple receiving house keys from an agent in front of city towers" style="inset:0;background:radial-gradient(ellipse at 50% 40%,rgba(255,255,255,.25),transparent 60%)"></div>
  <div class="abs logo" style="left:120px;top:45px"><span class="logo-mark"></span>Bright Harbor</div>
  <div class="abs social" style="left:822px;top:27px;background:#3b5bb5"></div>
  <div class="abs social" style="left:866px;top:27px;background:#d2327a"></div>
  <svg class="abs" style="left:934px;top:24px" width="26" height="26" viewBox="0 0 24 24" fill="none" stroke="#fff" stroke-width="1.6"><path d="M5 3h4l2 5-3 2a11 11 0 0 0 6 6l2-3 5 2v4a2 2 0 0 1-2 2A17 17 0 0 1 3 5a2 2 0 0 1 2-2z"/></svg>
  <div class="abs" style="left:973px;top:18px;color:#fff;font-size:12px;line-height:1.3">Call Us<br><b style="font-size:15px;font-weight:600">555.214.7730</b></div>
  <nav class="abs nav" style="left:0;width:1200px;height:20px">
    <span style="left:537px;top:-3px;width:24px;height:22px;border:3px solid var(--orange);border-radius:3px"></span>
    <span class="sep" style="left:590px"></span>
    <span style="left:620px">PRICING</span>
    <span class="sep" style="left:703px"></span>
    <span style="left:735px">SERVICES</span>
    <span class="sep" style="left:830px"></span>
    <span style="left:862px">PROPERTIES</span>
    <span class="sep" style="left:980px"></span>
    <span style="left:1010px">CONTACT</span>
  </nav>
  <div class="abs hero-arrow" style="left:158px;top:287px"><svg width="16" height="16" viewBox="0 0 16 16" fill="none" stroke="#fff" stroke-width="2"><path d="M10 3 5 8l5 5"/></svg></div>
  <div class="abs hero-arrow" style="left:1003px;top:287px"><svg width="16" height="16" viewBox="0 0 16 16" fill="none" stroke="#fff" stroke-width="2"><path d="m6 3 5 5-5 5"/></svg></div>
  <h1 class="abs center">Rental Solutions</h1>
  <div class="abs center sub">For Residential Properties</div>
</section>
<svg class="abs" style="left:0;top:600px" width="1200" height="90" viewBox="0 0 1200 90" preserveAspectRatio="none">
  <polyline points="0,76 600,57 1200,76" fill="none" stroke="#2f4f9f" stroke-width="5"/>
  <polygon points="0,78 600,62 1200,78 1200,90 0,90" fill="#ffffff"/>
</svg>

<!-- INTRO -->
<section class="intro">
  <div class="abs intro-photo" role="img" aria-label="Family sitting together on the floor of their new home"></div>
  <div class="abs intro-shadow"></div>
  <div class="abs" style="left:640px;top:690px;width:58px;height:50px;border:3px solid #c5c9d1;border-radius:4px"></div>
  <h2 class="abs intro-text">Short-Term Rental Management.</h2>
  <p class="abs intro-text lead">Integrated, end-to-end, rental solutions for residential properties.</p>
  <p class="abs intro-text body">Lorem Ipsum has been the industry's standard dummy text ever since the 1500s Lorem Ipsum is simply dummy text of the printing and typesetting industry. Lorem Ipsum is simply dummy text of the printing and typesetting industry.</p>
  <div class="btn btn-solid" style="left:641px;top:1053px;width:160px;height:43px">Learn More <svg width="20" height="10" viewBox="0 0 20 10" fill="none" stroke="#fff" stroke-width="1.5"><path d="M0 5h18M14 1l4 4-4 4"/></svg></div>
</section>

<!-- SERVICES -->
<section class="abs services" role="img" aria-label="Blue-tinted background photo of a family at home"></section>
<svg class="abs" style="left:0;top:1220px" width="1200" height="90" viewBox="0 0 1200 90" preserveAspectRatio="none">
  <polygon points="0,0 1200,0 1200,78 770,10 0,78" fill="#ffffff"/>
  <polygon points="0,78 770,10 1200,78 1200,90 770,26 0,90" fill="#c9ccd4"/>
</svg>
<h2 class="abs center" style="top:1340px;font-size:38px;font-weight:600;color:#fff">Services &amp; Solutions</h2>

<div class="svc" style="left:127px;top:1418px">
  <div class="svc-icon"><svg width="38" height="38" viewBox="0 0 24 24" fill="none" stroke="#fff" stroke-width="1.4"><circle cx="12" cy="7" r="3"/><path d="M6 20v-3a6 6 0 0 1 12 0v3M4 20h16"/></svg></div>
  <h3>One-on-One<br>Consultation</h3>
  <p style="opacity:.75">We take a personalized approach to our business and that starts from the beginning</p>
</div>
<div class="svc active" style="left:453px;top:1418px">
  <div class="svc-icon"><svg width="38" height="38" viewBox="0 0 24 24" fill="none" stroke="#3c5fb1" stroke-width="1.4"><rect x="5" y="3" width="14" height="18" rx="2"/><path d="M8 8h2v2H8zM12 9h4M8 13h2v2H8zM12 14h4"/></svg></div>
  <h3>Listing/Bright Harbor<br>Management App</h3>
  <p>The listing is the backbone to the success of any property. We create a listing only after visiting</p>
</div>
<div class="svc" style="left:779px;top:1418px">
  <div class="svc-icon"><svg width="38" height="38" viewBox="0 0 24 24" fill="none" stroke="#fff" stroke-width="1.4"><path d="M5 20V14M9 20v-8M13 20v-6M17 20V8M4 20h16M5 10l5-4 4 3 5-5"/></svg></div>
  <h3 style="margin-bottom:12px">Analytics</h3>
  <p>Through the collection and access to historical property performance in the local area, Bright Harbor is able to predict pricing</p>
</div>
<div class="svc" style="left:127px;top:1740px">
  <div class="svc-icon"><svg width="38" height="38" viewBox="0 0 24 24" fill="none" stroke="#fff" stroke-width="1.4"><circle cx="12" cy="9" r="6"/><path d="M9.5 11.5l5-5M10 7h.1M14 11h.1M3 18h5l3 2h6l4-3"/></svg></div>
  <h3 style="margin-bottom:12px">Strategic Pricing</h3>
  <p>Your success is our success. We will apply a strategic pricing model to your space to maximize revenue.</p>
</div>
<div class="svc" style="left:453px;top:1740px">
  <div class="svc-icon"><svg width="38" height="38" viewBox="0 0 24 24" fill="none" stroke="#fff" stroke-width="1.4"><rect x="4" y="5" width="16" height="15" rx="1"/><path d="M4 9h16M8 3v4M16 3v4M7 12h2M11 12h2M15 12h2M7 16h2M11 16h2M15 16h2"/></svg></div>
  <h3>Calendar<br>Management</h3>
  <p>Based on a proven strategy, we manage your calendars avail-ability and trip duration</p>
</div>
<div class="svc" style="left:779px;top:1740px">
  <div class="svc-icon"><svg width="38" height="38" viewBox="0 0 24 24" fill="none" stroke="#fff" stroke-width="1.4"><path d="M5 12a7 7 0 0 1 14 0v3h-3v-4h3M5 11h3v4H5v-3M17 17a4 4 0 0 1-4 3h-1"/></svg></div>
  <h3 style="margin-bottom:12px">24/7 Guest Support</h3>
  <p>Communicating with your guests is essential to your success and we have that mastered. From answering initial</p>
</div>
<div class="btn btn-solid" style="left:521px;top:2081px;width:159px;height:43px">Learn More <svg width="20" height="10" viewBox="0 0 20 10" fill="none" stroke="#fff" stroke-width="1.5"><path d="M0 5h18M14 1l4 4-4 4"/></svg></div>

<!-- PRICING -->
<section class="abs pricing"></section>
<h2 class="abs center" style="top:2290px;font-size:38px;font-weight:600;color:#fff">Pricing Plan</h2>

<div class="plan" style="left:185px;top:2415px;width:276px;height:366px">
  <h4>Small Business</h4>
  <div class="price"><sup>$</sup>49<small>/mo</small></div>
  <ul>
    <li><svg width="16" height="16" viewBox="0 0 16 16" fill="none" stroke="#3c5fb1" stroke-width="1.3"><circle cx="8" cy="8" r="6.5"/><path d="m5 8 2 2 4-4"/></svg>Lorem Ipsum is simply dummy</li>
    <li><svg width="16" height="16" viewBox="0 0 16 16" fill="none" stroke="#3c5fb1" stroke-width="1.3"><circle cx="8" cy="8" r="6.5"/><path d="m5 8 2 2 4-4"/></svg>Ipsum is simply dummy text</li>
    <li><svg width="16" height="16" viewBox="0 0 16 16" fill="none" stroke="#3c5fb1" stroke-width="1.3"><circle cx="8" cy="8" r="6.5"/><path d="m5 8 2 2 4-4"/></svg>Lorem Ipsum is simply</li>
  </ul>
  <div class="btn btn-ghost" style="left:70px;top:270px;width:138px;height:42px">Sign Up <svg width="20" height="10" viewBox="0 0 20 10" fill="none" stroke="#1f2230" stroke-width="1.5"><path d="M0 5h18M14 1l4 4-4 4"/></svg></div>
</div>
<div class="plan" style="left:462px;top:2385px;width:276px;height:428px;padding-top:33px;box-shadow:0 6px 30px rgba(0,0,0,.18)">
  <span class="tag">Recommended</span>
  <h4>Professional</h4>
  <div class="price"><sup>$</sup>219<small>/mo</small></div>
  <ul>
    <li><svg width="16" height="16" viewBox="0 0 16 16" fill="none" stroke="#3c5fb1" stroke-width="1.3"><circle cx="8" cy="8" r="6.5"/><path d="m5 8 2 2 4-4"/></svg>Lorem Ipsum is simply dummy</li>
    <li><svg width="16" height="16" viewBox="0 0 16 16" fill="none" stroke="#3c5fb1" stroke-width="1.3"><circle cx="8" cy="8" r="6.5"/><path d="m5 8 2 2 4-4"/></svg>Ipsum is simply dummy text</li>
    <li><svg width="16" height="16" viewBox="0 0 16 16" fill="none" stroke="#3c5fb1" stroke-width="1.3"><circle cx="8" cy="8" r="6.5"/><path d="m5 8 2 2 4-4"/></svg>Lorem Ipsum is simply</li>
  </ul>
  <div class="btn btn-solid" style="left:68px;top:302px;width:140px;height:42px">Sign Up <svg width="20" height="10" viewBox="0 0 20 10" fill="none" stroke="#fff" stroke-width="1.5"><path d="M0 5h18M14 1l4 4-4 4"/></svg></div>
</div>
<div class="plan" style="left:740px;top:2415px;width:276px;height:366px">
  <h4>Small Business</h4>
  <div class="price"><sup>$</sup>419<small>/mo</small></div>
  <ul>
    <li><svg width="16" height="16" viewBox="0 0 16 16" fill="none" stroke="#3c5fb1" stroke-width="1.3"><circle cx="8" cy="8" r="6.5"/><path d="m5 8 2 2 4-4"/></svg>Lorem Ipsum is simply dummy</li>
    <li><svg width="16" height="16" viewBox="0 0 16 16" fill="none" stroke="#3c5fb1" stroke-width="1.3"><circle cx="8" cy="8" r="6.5"/><path d="m5 8 2 2 4-4"/></svg>Ipsum is simply dummy text</li>
    <li><svg width="16" height="16" viewBox="0 0 16 16" fill="none" stroke="#3c5fb1" stroke-width="1.3"><circle cx="8" cy="8" r="6.5"/><path d="m5 8 2 2 4-4"/></svg>Lorem Ipsum is simply</li>
  </ul>
  <div class="btn btn-ghost" style="left:70px;top:270px;width:138px;height:42px">Sign Up <svg width="20" height="10" viewBox="0 0 20 10" fill="none" stroke="#1f2230" stroke-width="1.5"><path d="M0 5h18M14 1l4 4-4 4"/></svg></div>
</div>
<svg class="abs" style="left:0;top:2920px" width="1200" height="95" viewBox="0 0 1200 95" preserveAspectRatio="none">
  <polygon points="0,90 450,8 1200,90 1200,95 0,95" fill="#ffffff"/>
  <polyline points="0,90 450,8 1200,90" fill="none" stroke="#c4c7cf" stroke-width="5"/>
</svg>

<!-- FEATURED -->
<section class="featured">
  <h2 class="abs center">Featured Properties</h2>
  <div class="abs side-arrow" style="left:70px;top:3311px"><svg width="16" height="10" viewBox="0 0 16 10" fill="none" stroke="#555" stroke-width="1.4"><path d="M16 5H2M6 1 2 5l4 4"/></svg></div>
  <div class="abs side-arrow" style="left:1096px;top:3311px"><svg width="16" height="10" viewBox="0 0 16 10" fill="none" stroke="#555" stroke-width="1.4"><path d="M0 5h14M10 1l4 4-4 4"/></svg></div>

  <div class="prop" style="left:120px;top:3155px">
    <div class="prop-img" role="img" aria-label="Balcony view over a harbor with city skyline" style="background:linear-gradient(180deg,#8fb2d6,#6f8fa0 55%,#5c6a58)"></div>
    <h5>BEST VIEW! Harbor Point from<br>Top Floor, Lakeside</h5>
    <div class="meta"><b>$299</b>205 Reviews <span style="margin:0 8px;color:#ccc">|</span><span style="color:var(--star)">★★★★★</span></div>
    <div class="btn btn-grey">Learn More</div>
  </div>
  <div class="prop" style="left:447px;top:3155px">
    <div class="prop-img" role="img" aria-label="Modern open kitchen and living area" style="background:linear-gradient(135deg,#d8d2c8,#8c8c8c 60%,#4f4f55)"></div>
    <h5>BEST VIEW! Harbor Point from<br>Top Floor, Lakeside</h5>
    <div class="meta"><b>$299</b>205 Reviews <span style="margin:0 8px;color:#ccc">|</span><span style="color:var(--star)">★★★★★</span></div>
    <div class="btn btn-solid">Learn More</div>
  </div>
  <div class="prop" style="left:774px;top:3155px">
    <div class="prop-img" role="img" aria-label="Rooftop terrace lounge with city towers" style="background:linear-gradient(180deg,#c7d2dc,#8a9aa3 50%,#5e6f56)"></div>
    <h5>BEST VIEW! Harbor Point from<br>Top Floor, Lakeside</h5>
    <div class="meta"><b>$299</b>205 Reviews <span style="margin:0 8px;color:#ccc">|</span><span style="color:var(--star)">★★★★★</span></div>
    <div class="btn btn-grey">Learn More</div>
  </div>
  <div class="abs dots center" style="top:3578px"><i></i><i class="on"></i><i></i><i></i></div>
</section>

<!-- REVIEWS -->
<section class="reviews">
  <div class="abs reviews-bg" role="img" aria-label="Soft blurred photo of a family relaxing at home"></div>
  <svg class="abs" style="left:0;top:3655px" width="1200" height="90" viewBox="0 0 1200 90" preserveAspectRatio="none">
    <polygon points="0,0 1200,0 1200,85 780,12 0,85" fill="#ffffff"/>
    <polyline points="0,85 780,12 1200,85" fill="none" stroke="#2b2f3a" stroke-width="6"/>
  </svg>
  <h2 class="abs center">What Our Clients Say?</h2>

  <div class="review" style="left:162px;top:3865px"><div class="stars">★★★★★</div><h6>"SOLID Service! Vety consistent!"</h6><p>the printing and typesetting industry. Lorem Ipsum has been the industry's standard dummy text ever since the 1500s Lorem Ipsum!</p></div>
  <div class="review" style="left:462px;top:3865px"><div class="stars">★★★★★</div><h6>"SOLID Service! Vety consistent!"</h6><p>the printing and typesetting industry. Lorem Ipsum has been the industry's standard dummy text ever since the 1500s Lorem Ipsum!</p></div>
  <div class="review" style="left:762px;top:3865px"><div class="stars">★★★★★</div><h6>"SOLID Service! Vety consistent!"</h6><p>the printing and typesetting industry. Lorem Ipsum has been the industry's standard dummy text ever since the 1500s Lorem Ipsum!</p></div>

  <div class="person" style="left:200px;top:4075px"><div class="avatar" role="img" aria-label="Client portrait"></div><b>Marcus Ellery</b>Web Development</div>
  <div class="person" style="left:500px;top:4075px"><div class="avatar" role="img" aria-label="Client portrait"></div><b>Marcus Ellery</b>Web Development</div>
  <div class="person" style="left:800px;top:4075px"><div class="avatar" role="img" aria-label="Client portrait"></div><b>Marcus Ellery</b>Web Development</div>
  <div class="abs dots center" style="top:4208px"><i></i><i class="on"></i><i></i><i></i></div>
</section>

<!-- FOOTER -->
<footer class="abs footer"></footer>
<svg class="abs" style="left:0;top:4268px" width="1200" height="72" viewBox="0 0 1200 72" preserveAspectRatio="none">
  <polygon points="0,72 0,70 320,40 880,0 1200,70 1200,72" fill="#262b3b"/>
</svg>
<div class="abs logo" style="left:120px;top:4428px;font-size:32px"><span class="logo-mark" style="width:32px;height:32px"></span>Bright Harbor</div>
<div class="abs" style="left:165px;top:4500px;display:flex;gap:14px">
  <i style="width:14px;height:14px;border-radius:50%;background:#fff;display:block"></i>
  <i style="width:14px;height:14px;border-radius:50%;background:#fff;display:block"></i>
  <i style="width:14px;height:14px;border-radius:50%;border:2px solid #fff;display:block"></i>
</div>

<h6 class="abs" style="left:410px;top:4378px;color:#fff;font-size:14px;font-weight:600">Contact Us</h6>
<svg class="abs" style="left:410px;top:4420px" width="14" height="16" viewBox="0 0 14 16" fill="none" stroke="#fff" stroke-width="1.3"><path d="M7 15s5-5 5-9A5 5 0 0 0 2 6c0 4 5 9 5 9z"/><circle cx="7" cy="6" r="1.8"/></svg>
<div class="abs" style="left:438px;top:4418px;font-size:12px;color:#d5d8df;line-height:1.8">48 Alder Row #3B<br>Fairview 20417</div>
<svg class="abs" style="left:410px;top:4472px" width="15" height="15" viewBox="0 0 24 24" fill="#fff"><path d="M5 3h4l2 5-3 2a11 11 0 0 0 6 6l2-3 5 2v4a2 2 0 0 1-2 2A17 17 0 0 1 3 5a2 2 0 0 1 2-2z"/></svg>
<div class="abs" style="left:438px;top:4472px;font-size:12px;color:#d5d8df">(555) 310-4482</div>
<svg class="abs" style="left:410px;top:4510px" width="16" height="12" viewBox="0 0 16 12" fill="none" stroke="#fff" stroke-width="1.3"><rect x=".7" y=".7" width="14.6" height="10.6"/><path d="m1 1 7 6 7-6"/></svg>
<div class="abs" style="left:438px;top:4508px;font-size:12px;color:#d5d8df">hello@brightharbor.ca</div>

<h6 class="abs" style="left:662px;top:4378px;color:#fff;font-size:14px;font-weight:600">Company</h6>
<div class="abs" style="left:662px;top:4412px;font-size:12px;color:#d5d8df;line-height:1.9">Home<br>Pricing<br>Services<br>Properties<br>Contact Us</div>

<h6 class="abs" style="left:840px;top:4378px;color:#fff;font-size:14px;font-weight:600">Stil have questions?</h6>
<div class="abs" style="left:840px;top:4414px;width:240px;font-size:12px;color:#d5d8df;line-height:1.8">A repesentative will aswer your questions as soon as possible.</div>
<div class="abs footer-phone" style="color:#fff"><i><svg width="18" height="18" viewBox="0 0 24 24" fill="none" stroke="#fff" stroke-width="1.6"><path d="M5 3h4l2 5-3 2a11 11 0 0 0 6 6l2-3 5 2v4a2 2 0 0 1-2 2A17 17 0 0 1 3 5a2 2 0 0 1 2-2z"/></svg></i>555.214.7730</div>

<div class="abs" style="left:0;top:4584px;width:1200px;height:1px;background:rgba(255,255,255,.12)"></div>
<div class="abs" style="left:120px;top:4612px;font-size:12px;color:#d5d8df;display:flex;align-items:center;gap:6px">Copyright 2020 <span style="margin-left:22px;width:12px;height:12px;border:2px solid #fff;display:inline-block"></span><b style="color:#fff;font-weight:600">Bright Harbor.</b> All Rights Reserved.</div>
<div class="abs" style="left:810px;top:4612px;font-size:12px;color:#d5d8df">Privacy Policy <span style="margin:0 8px;color:#666">|</span> Terms Of Services</div>

</body>
</html>
```